Design extract to a timeless cook-book with a modern look.

Hi,

(This is no bookcover-design.)

I need help with a book design - a few pages that will go as a proposal to a publishing company.

The project has three segments.
1. One is the story of the person behind it (its a sad story that ends well - I have replaced it with Lorem Ipsum) and,
2. the second is a cookery-segment with recipe and,
3. lastly a table of contents for the same.

The right order in the book would be to start with:
1. Table of contents (I upload two files - the one in Swedish is the one to choose. The other is for you to know what it is)
2. The story. The Lorem Ipsum text.
3. Lastly the main part - cooking-recipe. Here you see boxes with one line of text for a future picture. You can just think about the leave space, for a later inserted picture.

Would like a modern look - but still a touch of a classic cookery-book. Please give examples of page layout in the three segments. Also think about the design of the books figures in the corner. Feel free to act upon it.
I am sorry Im in a hurry with this project - but please do not come back with a proposal made in 15 min. It will not go thru.

You are mostly welcome to ask me questions. Good luck!

Target Market(s)

Adults - intrested in cooking.

Industry/Entity Type

It Company

Font styles to use
Serif
Sans Serif
Script

Colors

Designer to choose colors to be used in the design.

Requirements
Must have
• The feeling of a cook-book. Easy to read. Format printed will be (or around) A4 (210 x 297 mm.)
• - All three segments.

```html
<!DOCTYPE html>
<html lang="sv">
<head>
<meta charset="utf-8">
<title>Kokbok – uppslag</title>
<link rel="stylesheet" href="https://fonts.googleapis.com/css2?family=Oswald:wght@400;600;700&family=Source+Sans+3:wght@400;600;700&display=swap">
<style>
:root{
  --bg:#ececec;
  --paper:#ffffff;
  --ink:#3a3a3a;
  --muted:#7a7a7a;
  --red:#b8322a;
  --slate:#55585c;
  --slate-dark:#45484c;
  --rule:#d6d6d6;
}
*{box-sizing:border-box;margin:0;padding:0}
html,body{width:1200px;height:2432px;overflow:hidden;background:var(--bg)}
body{position:relative;font-family:"Source Sans 3",Arial,sans-serif;color:var(--ink)}
.spread{position:absolute;left:32px;width:1136px;display:flex;box-shadow:0 2px 8px rgba(0,0,0,.18)}
.spread--toc{top:16px;height:856px}
.spread--recipe-a{top:888px;height:852px}
.spread--recipe-b{top:1760px;height:672px}
.page{position:relative;width:568px;height:100%;background:var(--paper);overflow:hidden}
.page--dark{background:var(--slate);color:#e6e6e6}
.folio{position:absolute;bottom:22px;font:600 11px "Oswald",sans-serif;letter-spacing:1px;color:var(--muted);display:flex;align-items:center;gap:6px}
.folio::before{content:"";width:8px;height:8px;background:var(--red)}
.folio--left{left:40px}.folio--right{right:40px}
.page--dark .folio{color:#cfcfcf}

/* contents */
.toc-band{height:56px;background:var(--slate-dark);color:#fff;font:600 20px "Oswald",sans-serif;letter-spacing:2px;padding:16px 40px}
.toc{padding:28px 40px 0}
.toc-section{display:flex;justify-content:space-between;align-items:flex-end;border-bottom:1px solid var(--rule);padding:14px 0 6px;font:600 14px "Oswald",sans-serif;color:var(--red);letter-spacing:1px}
.toc-section span:last-child{color:var(--ink)}
.toc-sub{font-size:12px;color:var(--muted);padding:4px 0 6px;border-bottom:1px solid var(--rule)}
.toc-heading{margin-top:36px;background:var(--red);color:#fff;font:600 15px "Oswald",sans-serif;letter-spacing:1px;padding:7px 10px}
.toc-cols{display:flex;gap:20px}
.toc-col{flex:1}
.toc-col-head{display:flex;justify-content:space-between;font:600 13px "Oswald",sans-serif;padding:10px 0 6px;border-bottom:2px solid var(--ink)}
.toc-day{padding:8px 0 6px;border-bottom:1px solid var(--rule)}
.toc-day b{display:block;font:600 12px "Oswald",sans-serif;color:var(--red)}
.toc-day span{display:flex;justify-content:space-between;font-size:11px;color:var(--muted)}
.toc-note{font-size:10px;color:var(--muted);text-align:center;margin-top:14px}

/* story */
.story{padding:48px 40px 0}
.story-date{font:600 20px "Oswald",sans-serif;letter-spacing:1px;color:#fff;border-bottom:1px solid #8a8d91;padding-bottom:10px;margin-bottom:18px}
.story-text{column-count:2;column-gap:24px;font-size:11.5px;line-height:1.55;text-align:justify;height:520px}
.story-text p{margin-bottom:10px}
.picture-slot{position:absolute;right:40px;bottom:60px;width:232px;height:210px;background:#fff;display:flex;align-items:center;justify-content:center;font-size:17px;color:#9a9a9a}

/* recipe */
.recipe{padding:40px 40px 0}
.recipe-title{font:700 28px/1.08 "Oswald",sans-serif;color:var(--red);letter-spacing:.5px;text-transform:uppercase}
.recipe-kicker{font:600 12px "Oswald",sans-serif;letter-spacing:1px;color:var(--ink);margin:14px 0 8px}
.recipe-intro{column-count:2;column-gap:22px;font-size:11px;line-height:1.5;text-align:justify;margin-bottom:18px}
.recipe-intro p{margin-bottom:6px}
.recipe-body{display:flex;gap:22px}
.recipe-col{flex:1}
.label{font:600 12px "Oswald",sans-serif;letter-spacing:1px;border-bottom:2px solid var(--red);padding-bottom:4px;margin-bottom:8px}
.ingredients{list-style:none;font-size:11px;line-height:1.6}
.ingredients li{border-bottom:1px solid var(--rule);padding:2px 0}
.steps{list-style:none;counter-reset:s;font-size:11px;line-height:1.45}
.steps li{counter-increment:s;position:relative;padding:0 0 7px 18px}
.steps li::before{content:counter(s)".";position:absolute;left:0;color:var(--red);font-weight:700}
.photo{border-radius:0}
.photo--small{height:74px;margin:10px 0;background:linear-gradient(120deg,#b9463a,#d7b49a 55,#6d8d4e)}
.photo--row{display:flex;gap:6px;margin:8px 0}
.photo--row div{flex:1;height:64px}
.tone-a{background:linear-gradient(135deg,#c0584b,#e0b8a2)}
.tone-b{background:linear-gradient(135deg,#d44a2e,#8e2a1e)}
.tone-c{background:linear-gradient(135deg,#e8dcc0,#b69c6f)}
.dish{position:absolute;left:28px;right:28px;top:36px;height:420px;background:radial-gradient(circle at 50% 50%,#c65a3d 0,#b4482e 35%,#e8ddd2 62%,#f6f2ec 100%)}
.dish--b{top:380px;height:260px}
.dish-top{position:absolute;left:28px;right:28px;top:36px;height:300px;background:radial-gradient(circle at 50% 60%,#c04a2f 0,#d98a5f 40%,#f2ebe3 75%)}
</style>
</head>
<body>

<section class="spread spread--toc">
  <article class="page">
    <header class="toc-band">INNEHÅLL</header>
    <div class="toc">
      <div class="toc-section"><span>BAKGRUND</span><span>3</span></div>
      <div class="toc-sub">Om personen bakom boken</div>
      <div class="toc-section"><span>PRINCIP OCH MÅLSÄTTNING</span><span>5</span></div>
      <div class="toc-sub">Tankar om mat och vardag</div>
      <div class="toc-section"><span>UTGÅNGSMATERIAL</span><span>7</span></div>
      <div class="toc-sub">Basvaror i skafferiet</div>
      <div class="toc-heading">RECEPTSAMLING</div>
      <div class="toc-cols">
        <div class="toc-col">
          <div class="toc-col-head"><span>LUNCHRECEPT</span><span>VECKA 1</span></div>
          <div class="toc-day"><b>Måndag</b><span>Köttfärssås med pasta<em>12</em></span></div>
          <div class="toc-day"><b>Tisdag</b><span>Vegetarisk soppa<em>14</em></span></div>
          <div class="toc-day"><b>Onsdag</b><span>Fisk i ugn<em>16</em></span></div>
          <div class="toc-day"><b>Torsdag</b><span>Ärtsoppa med fläsk<em>18</em></span></div>
          <div class="toc-day"><b>Fredag</b><span>Kyckling med ris<em>20</em></span></div>
          <div class="toc-day"><b>Lördag</b><span>Enkel billig köttfärssås<em>22</em></span></div>
          <div class="toc-day"><b>Söndag</b><span>Stekt lax med potatis<em>24</em></span></div>
        </div>
        <div class="toc-col">
          <div class="toc-col-head"><span>LUNCHRECEPT</span><span>VECKA 2</span></div>
          <div class="toc-day"><b>Måndag</b><span>Pannkakor med sylt<em>26</em></span></div>
          <div class="toc-day"><b>Tisdag</b><span>Linsgryta<em>28</em></span></div>
          <div class="toc-day"><b>Onsdag</b><span>Fiskgratäng<em>30</em></span></div>
          <div class="toc-day"><b>Torsdag</b><span>Korv stroganoff<em>32</em></span></div>
          <div class="toc-day"><b>Fredag</b><span>Tacos med bönor<em>34</em></span></div>
          <div class="toc-day"><b>Lördag</b><span>Köttbullar med potatis<em>36</em></span></div>
          <div class="toc-day"><b>Söndag</b><span>Helstekt kyckling<em>38</em></span></div>
        </div>
      </div>
      <p class="toc-note">* Recepten listas i veckoordning</p>
    </div>
    <span class="folio folio--left">2</span>
  </article>
  <article class="page page--dark">
    <div class="story">
      <h2 class="story-date">1 SEPTEMBER 2013</h2>
      <div class="story-text">
        <p>Lorem ipsum dolor sit amet, consectetur adipiscing elit. Integer nec odio praesent libero, sed cursus ante dapibus diam. Sed nisi nulla quis sem at nibh elementum imperdiet. Duis sagittis ipsum, praesent mauris fusce nec tellus sed augue semper porta. Mauris massa vestibulum lacinia arcu eget nulla.</p>
        <p>Class aptent taciti sociosqu ad litora torquent per conubia nostra, per inceptos himenaeos. Curabitur sodales ligula in libero sed dignissim lacinia nunc. Curabitur tortor pellentesque nibh aenean quam in scelerisque sem at dolor maecenas mattis sed convallis tristique sem.</p>
        <p>Proin ut ligula vel nunc egestas porttitor. Morbi lectus risus, iaculis vel suscipit quis, luctus non massa. Fusce ac turpis quis ligula lacinia aliquet. Mauris ipsum nulla metus metus ullamcorper vel tincidunt sed euismod in nibh quisque volutpat condimentum velit.</p>
        <p>Nam nec ante sed lacinia urna non tincidunt mattis, tortor neque adipiscing diam, a cursus ipsum ante quis turpis. Nulla facilisi ut fringilla suspendisse potenti nunc feugiat mi a tellus consequat imperdiet vestibulum sapien proin quam etiam ultrices.</p>
        <p>Suspendisse in justo eu magna luctus suscipit. Sed lectus integer euismod lacus luctus magna. Quisque cursus, metus vitae pharetra auctor, sem massa mattis sem, at interdum magna augue eget diam vestibulum ante ipsum primis in faucibus orci luctus et ultrices posuere cubilia curae.</p>
        <p>Morbi lacinia molestie dui praesent blandit dolor sed non quam in vel mi sit amet augue congue elementum.</p>
      </div>
    </div>
    <div class="picture-slot">Picture here</div>
    <span class="folio folio--right">3</span>
  </article>
</section>

<section class="spread spread--recipe-a">
  <article class="page">
    <div class="recipe">
      <h1 class="recipe-title">Extrasnabb och enkel köttfärssås med valfri pasta</h1>
      <p class="recipe-kicker">TACK OCH LOV FÖR RECEPTET</p>
      <div class="recipe-intro">
        <p>När man har ont om tid och ändå vill laga något gott är det här rätten att ta till. Den går fort att göra, kräver få ingredienser och passar hela familjen.</p>
        <p>Välj den pasta du tycker bäst om och servera med riven ost och en grön sallad vid sidan om. Såsen går bra att frysa i portioner.</p>
        <p>Mitt tips är att låta såsen puttra några extra minuter om tiden finns, då blir smaken rundare och mustigare.</p>
      </div>
      <div class="recipe-body">
        <div class="recipe-col">
          <h3 class="label">INGREDIENSER</h3>
          <ul class="ingredients">
            <li>4 portioner pasta efter smak</li>
            <li>400 g köttfärs</li>
            <li>1 burk krossade tomater</li>
            <li>1 gul lök, salt och peppar</li>
          </ul>
          <div class="photo photo--small" role="img" aria-label="Ingredienser till köttfärssåsen"></div>
        </div>
        <div class="recipe-col">
          <h3 class="label">TILLAGA SÅ HÄR</h3>
          <ol class="steps">
            <li>Koka pastan enligt anvisning på förpackningen.</li>
            <li>Hacka löken fint och fräs den mjuk i lite olja.</li>
            <li>Tillsätt köttfärsen och bryn den ordentligt.</li>
            <li>Häll i tomaterna och låt sjuda i tio minuter.</li>
            <li>Smaka av med salt och peppar och servera med pastan.</li>
          </ol>
        </div>
      </div>
    </div>
    <span class="folio folio--left">12</span>
  </article>
  <article class="page">
    <div class="dish" role="img" aria-label="Tallrik med pasta och köttfärssås"></div>
    <span class="folio folio--right">13</span>
  </article>
</section>

<section class="spread spread--recipe-b">
  <article class="page">
    <div class="recipe">
      <h1 class="recipe-title">Enkel och billig köttfärssås</h1>
      <p class="recipe-kicker">4 PORTIONER</p>
      <div class="recipe-body">
        <div class="recipe-col">
          <h3 class="label">INGREDIENSER</h3>
          <ul class="ingredients">
            <li>500 g nötfärs</li>
            <li>1 gul lök, 2 vitlöksklyftor</li>
            <li>1 burk krossade tomater</li>
            <li>2 msk tomatpuré</li>
            <li>1 dl vatten, 1 buljongtärning</li>
            <li>Salt, svartpeppar och oregano</li>
          </ul>
          <div class="photo--row">
            <div class="tone-a" role="img" aria-label="Köttfärs"></div>
            <div class="tone-b" role="img" aria-label="Tomatsås"></div>
            <div class="tone-c" role="img" aria-label="Lök och vitlök"></div>
          </div>
        </div>
        <div class="recipe-col">
          <h3 class="label">GÖR SÅ HÄR</h3>
          <ol class="steps">
            <li>Skala och hacka lök och vitlök.</li>
            <li>Fräs löken i olja tills den är blank.</li>
            <li>Lägg i färsen och bryn den i några minuter.</li>
            <li>Rör ner tomatpuré och låt den fräsa med.</li>
            <li>Tillsätt tomater, vatten och buljong.</li>
            <li>Krydda och låt sjuda under lock i femton minuter.</li>
            <li>Smaka av och servera med valfri pasta eller ris.</li>
          </ol>
        </div>
      </div>
    </div>
    <span class="folio folio--left">22</span>
  </article>
  <article class="page">
    <div class="dish-top" role="img" aria-label="Köttfärssås serverad på tallrik"></div>
    <div class="dish dish--b" role="img" aria-label="Närbild på pasta med köttfärssås"></div>
  </article>
</section>

</body>
</html>
```